Web design for software company

I'm a software developer that designs high end specialist web applications, mobile apps and user friendly applications for medium to large customers. I integrate different systems together within a company and provide web based applications or mobile apps to view and edit information in that web of linked systems.

I currently work alone, basically selling my time on specialist projects, but also build my own software solutions which I eventually want to put into the market.

My company name is Quarrymind (lowercase 'L' for logic) and I work from the Netherlands. I've attached my current logo which is basically just text in VOXbox font. Current colours are mustard yellow and grey, but i'm open to other options to better fit the web design.

I've got a sort of slogan: "Specialized software development" - better ideas are welcome. The slogan in the logo attachment is older.

I'm looking for a site design that reflects my work as being on the cutting edge of technology, but being clear and simple. My thinking with the name Quarrymind is that it refers to the underlying mechanism and logic of software.

The site will not be text heavy, so some kind of large graphic to do with software design is welcome. I expect about 4 or 5 main pages or sections of the site in which i'll eventually add things like a blog or contact info etc.

Industry/Entity Type

It Company

Number of Pages Required

1 page

Font styles to use
Sans Serif

Requirements
Nice to have
• A large graphic or photo relevant to my focus as a software developer. Something that shows connecting of software systems with perhaps a variety of devices/browsers that would display data from that cloud of systems.
• Something like these (allthough these are ugly - but the idea is what i mean):
• http://st4.pixelvaultimg.example/2000817/22458/i/450/pixelvaultimg_224581193-Cloud-computing-user-interface.jpg
• http://business.tallwick.example/images/modules/mobile-device-policy-design-banner.png
• https://www.pagecrafta.example/images/responsive-web-design.jpg
• http://www.brevanto.example/images/web_apps.png
• https://www.keymurra.example/assets/img/product/web-app@2x.png?v2
Should not have
• Photographs of smiling happy people looking at a screen that make it look like it's a huge business with many offices. I'm a one-man company which could perhaps grow a little bit, but i want to focus on my expertise instead of size.

```html
<!DOCTYPE html>
<html lang="en">
<head>
<meta charset="utf-8">
<title>Quarrymind — Specialised Software Development</title>
<link rel="stylesheet" href="https://fonts.googleapis.com/css2?family=Arimo:wght@400;700&display=swap">
<style>
  :root {
    --black: #000000;
    --white: #ffffff;
    --mustard: #f5d80f;
    --panel: rgba(8, 8, 8, 0.78);
    --photo-top: #4a4a4c;
    --photo-mid: #6b5a4c;
    --photo-bottom: #5a3f2e;
  }
  * { box-sizing: border-box; margin: 0; padding: 0; }
  html, body {
    width: 1200px;
    height: 926px;
    overflow: hidden;
    background: var(--black);
    font-family: "Arimo", Arial, sans-serif;
  }
  .page {
    position: relative;
    width: 1200px;
    height: 926px;
    overflow: hidden;
  }
  .site-header {
    position: absolute;
    top: 0; left: 0;
    width: 1200px;
    height: 112px;
    background: var(--black);
    z-index: 2;
  }
  .brand {
    position: absolute;
    left: 26px;
    top: 34px;
    display: flex;
    flex-direction: column;
  }
  .brand-name {
    color: var(--mustard);
    font-weight: 700;
    font-size: 50px;
    line-height: 42px;
    letter-spacing: 4px;
  }
  .brand-tagline {
    align-self: flex-end;
    color: var(--white);
    font-size: 10px;
    letter-spacing: 0.5px;
    margin-top: 3px;
  }
  .main-nav {
    position: absolute;
    right: 28px;
    top: 67px;
    display: flex;
    align-items: center;
    color: var(--white);
    font-size: 20px;
    line-height: 24px;
  }
  .main-nav a { color: var(--white); text-decoration: none; }
  .main-nav .divider { margin: 0 12px; }
  .hero-photo {
    position: absolute;
    top: 112px; left: 0;
    width: 1200px;
    height: 814px;
    background:
      radial-gradient(ellipse at 85% 45%, rgba(190,190,190,0.55), transparent 45%),
      radial-gradient(ellipse at 15% 25%, rgba(200,200,205,0.45), transparent 40%),
      radial-gradient(ellipse at 70% 85%, rgba(220,225,230,0.5), transparent 35%),
      linear-gradient(180deg, var(--photo-top) 0%, var(--photo-mid) 50%, var(--photo-bottom) 100%);
  }
  .hero-panel {
    position: absolute;
    left: 145px;
    top: 188px;
    width: 910px;
    height: 644px;
    background: var(--panel);
    z-index: 1;
  }
  .hero-title {
    position: absolute;
    left: 41px;
    top: 21px;
    color: var(--white);
    font-weight: 700;
    font-size: 71px;
    line-height: 67px;
    letter-spacing: 0;
  }
  .hero-rule {
    position: absolute;
    left: 43px;
    top: 251px;
    width: 825px;
    height: 4px;
    background: var(--white);
  }
  .hero-text {
    position: absolute;
    left: 43px;
    top: 286px;
    width: 830px;
    color: var(--white);
    font-weight: 700;
    font-size: 18px;
    line-height: 35.3px;
    letter-spacing: 4.4px;
  }
  .social-links {
    position: absolute;
    left: 919px;
    top: 860px;
    display: flex;
    gap: 9px;
    z-index: 1;
  }
  .social-dot {
    width: 38px;
    height: 38px;
    border-radius: 50%;
    background: var(--white);
  }
</style>
</head>
<body>
<div class="page">
  <header class="site-header">
    <div class="brand">
      <span class="brand-name">QUARRYMIND</span>
      <span class="brand-tagline">CUSTOM SOFTWARE SOLUTIONS</span>
    </div>
    <nav class="main-nav">
      <a href="#">HOME</a><span class="divider">I</span>
      <a href="#">ABOUT</a><span class="divider">I</span>
      <a href="#">SERVICES</a><span class="divider">I</span>
      <a href="#">CONTACT</a>
    </nav>
  </header>

  <div class="hero-photo" role="img" aria-label="Photo of a desktop computer, laptop, tablet, keyboard and mouse on a wooden desk, showing web application screens"></div>

  <section class="hero-panel">
    <h1 class="hero-title">SPECIALISED<br>SOFWARE<br>DEVELOPEMENT</h1>
    <div class="hero-rule"></div>
    <p class="hero-text">I'm a paragraph. Click here to add your own text and edit me. It’s easy. Just click “Edit Text” or double click me and you can start adding your own content and make changes to the font. Feel free to drag and drop me anywhere you like on your page. I’m a great place for you to tell a story and let your users know a little more about you.</p>
  </section>

  <div class="social-links" aria-label="Social links">
    <span class="social-dot"></span>
    <span class="social-dot"></span>
    <span class="social-dot"></span>
  </div>
</div>
</body>
</html>
```